Wine Label Design for Ferrant Estate

I need a front and back label for a new wine I am making. I am looking for a classic, elegant and serious wine label. I would like the label to be white with blue and black writing. The blue will be the distinction in the label. The color of blue will be unique and catch the eye. The font of the writing will be unique and could also serve as the brand image for Ferrant Estate. The label can have a design but should be simple and distinct. I envision the paper quality of the label to textured, high quality and add to the overall image of the label.
The label will be timeless. The price of this wine will be $85.00 a bottle, and the label should match a higher priced wine. This wine is family owned and operated.
The writing on the front and back label will be:

FRONT Label-

Ferrant Estate

Howell Mountain

Napa Valley

2022 Cabernet Sauvignon

Back Label-

Cellared and Bottled by Ferrant Estate, Angwin, CA 94508

GOVERNMENT WARNING: (1) According to the Surgeon General, women should not drink alcoholic beverages during pregnancy because of the risk of birth defects. (2) Consumption of alcoholic beverages impairs your ability to drive a car or operate machinery, and may cause health problems.

Alc. 14.5% by Vol.

750 ml

Contains Sulfites

```html
<!DOCTYPE html>
<html lang="en">
<head>
<meta charset="utf-8">
<title>Ferrant Estate — Front Label</title>
<link rel="stylesheet" href="https://fonts.googleapis.com/css2?family=Grenze+Gotisch:wght@500;700&family=Marcellus&display=swap">
<style>
  :root {
    --backdrop: #1c0606;
    --paper: #f7f6f2;
    --paper-shade: #ecebe6;
    --ink-black: #1b1c22;
    --ink-blue: #4a4f8f;
    --gold: #b78a4a;
    --gold-soft: #d9c29a;
  }
  * { margin: 0; padding: 0; box-sizing: border-box; }
  html, body {
    width: 1200px; height: 860px; overflow: hidden;
    background: var(--backdrop);
  }
  .canvas {
    width: 1200px; height: 860px;
    display: flex; align-items: center; justify-content: center;
  }
  .label {
    position: relative;
    width: 620px; height: 780px;
    background: radial-gradient(ellipse at 40% 30%, var(--paper) 0%, var(--paper-shade) 100%);
    box-shadow: 0 20px 50px rgba(0,0,0,.5);
  }
  .label__frame {
    position: absolute; inset: 22px;
    border: 1.5px solid var(--gold);
  }
  .label__ornament {
    position: absolute; width: 90px; height: 44px;
    background: var(--gold-soft); opacity: .55; border-radius: 4px;
  }
  .label__ornament--top { top: 12px; right: 60px; }
  .label__ornament--side { left: 12px; top: 300px; width: 26px; height: 130px; }
  .label__ornament--bottom { bottom: 12px; left: 60px; }
  .label__content {
    position: absolute; inset: 0;
    display: flex; flex-direction: column; align-items: center;
    padding-top: 80px;
  }
  .brand-mark {
    display: flex; align-items: center; gap: 10px;
    font-family: "Marcellus", serif;
    font-size: 18px; letter-spacing: 3px;
    color: var(--ink-black);
    text-transform: uppercase;
  }
  .brand-mark__dot {
    width: 10px; height: 10px; border-radius: 50%;
    background: var(--ink-blue);
  }
  .wordmark {
    margin-top: 40px;
    font-family: "Grenze Gotisch", serif;
    font-weight: 700;
    line-height: .9;
    text-align: center;
  }
  .wordmark__line { display: block; }
  .wordmark__line--first { font-size: 150px; color: var(--ink-black); }
  .wordmark__line--second { font-size: 130px; color: var(--ink-blue); }
  .appellation {
    margin-top: 34px;
    font-family: "Marcellus", serif;
    font-size: 38px; letter-spacing: 4px;
    color: var(--ink-black);
    text-align: center; line-height: 1.25;
  }
  .vintage {
    margin-top: 22px;
    font-family: "Grenze Gotisch", serif;
    font-weight: 500;
    font-size: 54px;
    color: var(--gold);
  }
  .varietal {
    margin-top: 10px;
    font-family: "Marcellus", serif;
    font-size: 26px; letter-spacing: 3px;
    color: var(--ink-black);
  }
</style>
</head>
<body>
  <main class="canvas">
    <section class="label">
      <div class="label__frame"></div>
      <div class="label__ornament label__ornament--top" role="img" aria-label="Gold filigree corner ornament"></div>
      <div class="label__ornament label__ornament--side" role="img" aria-label="Gold filigree side ornament"></div>
      <div class="label__ornament label__ornament--bottom" role="img" aria-label="Gold filigree corner ornament"></div>
      <div class="label__content">
        <div class="brand-mark"><span class="brand-mark__dot"></span>Ferrant Estate</div>
        <h1 class="wordmark">
          <span class="wordmark__line wordmark__line--first">Ferrant</span>
          <span class="wordmark__line wordmark__line--second">Estate</span>
        </h1>
        <p class="appellation">HOWELL MOUNTAIN<br>NAPA VALLEY</p>
        <p class="vintage">2022</p>
        <p class="varietal">CABERNET SAUVIGNON</p>
      </div>
    </section>
  </main>
</body>
</html>
```